Tralvo GmbH banner ad

Banner ad for Facebook Our company name (logo) Title: Transporter and bus rental Text: Without deposit, super prices

Target Market(s)

Rental

Requirements
Must have
• LOGO from us, Evt. A pair of transporters in the picture

```html
<!DOCTYPE html>
<html lang="de">
<head>
<meta charset="utf-8">
<title>Tralvo GmbH – Banner</title>
<link rel="stylesheet" href="https://fonts.googleapis.com/css2?family=Oswald:wght@300;400;500&display=swap">
<style>
  :root {
    --page-bg: #ececec;
    --banner-bg: #eeeff1;
    --facet: #e2e3e6;
    --brand-blue: #2a2fd0;
    --steel: #8199b5;
    --navy: #1c1f73;
    --ink: #262626;
    --divider: #cfd2d7;
    --photo-light: #c98a55;
    --photo-dark: #8a4f24;
  }
  * { margin: 0; padding: 0; box-sizing: border-box; }
  html, body {
    width: 1200px; height: 1200px; overflow: hidden;
    background: var(--page-bg);
    font-family: "Oswald", sans-serif;
  }
  .banner {
    position: absolute; left: 50px; top: 490px;
    width: 1100px; height: 220px;
    background: var(--banner-bg);
    overflow: hidden;
    box-shadow: 0 2px 8px rgba(0,0,0,0.12);
  }
  .banner-shapes { position: absolute; inset: 0; }
  .brand {
    position: absolute; left: 52px; top: 88px;
    display: flex; align-items: center; gap: 14px;
  }
  .brand-mark { width: 30px; height: 30px; background: var(--navy); }
  .brand-name {
    font-weight: 500; font-size: 38px; line-height: 1;
    color: var(--navy); letter-spacing: 0.5px;
  }
  .divider {
    position: absolute; left: 351px; top: 48px;
    width: 1px; height: 128px; background: var(--divider);
  }
  .headline {
    position: absolute; left: 385px; top: 40px;
    text-transform: uppercase; font-weight: 500;
    font-size: 44px; line-height: 50px;
  }
  .headline .line-dark { display: block; color: var(--ink); }
  .headline .line-steel { display: block; color: var(--steel); }
  .tagline {
    position: absolute; left: 383px; top: 142px;
    font-weight: 300; font-size: 32px; line-height: 1;
    color: var(--brand-blue);
  }
</style>
</head>
<body>
  <section class="banner">
    <svg class="banner-shapes" width="1100" height="220" viewBox="0 0 1100 220">
      <defs>
        <linearGradient id="productTone" x1="0" y1="0" x2="1" y2="1">
          <stop offset="0" stop-color="var(--photo-light)"/>
          <stop offset="1" stop-color="var(--photo-dark)"/>
        </linearGradient>
      </defs>
      <!-- background facets -->
      <polygon class="facet" points="140,30 330,0 520,70 300,220 150,170" fill="var(--facet)" opacity="0.7"/>
      <polygon class="facet" points="520,0 700,0 640,120" fill="var(--facet)" opacity="0.6"/>
      <!-- top-left accents -->
      <polygon class="accent-steel" points="40,0 232,0 242,26 36,26 0,90 0,62" fill="var(--steel)"/>
      <polygon class="accent-blue" points="0,0 40,0 0,92" fill="var(--brand-blue)"/>
      <!-- bottom bands -->
      <rect class="band-blue" x="0" y="208" width="240" height="12" fill="var(--brand-blue)"/>
      <rect class="band-steel" x="240" y="208" width="490" height="12" fill="var(--steel)"/>
      <!-- product frame -->
      <polygon class="accent-blue" points="708,175 790,175 835,220 722,220" fill="var(--brand-blue)"/>
      <polygon class="product-frame" points="741,14 1010,14 1100,214 835,220" fill="#ffffff" stroke="var(--navy)" stroke-width="2"/>
      <polygon class="accent-blue" points="1030,52 1068,52 1100,124 1100,212" fill="var(--brand-blue)"/>
      <rect class="product-photo" role="img" aria-label="Produktfoto: ein Paar braune Lederschuhe" x="738" y="38" width="305" height="155" rx="40" fill="url(#productTone)"/>
    </svg>

    <div class="brand">
      <span class="brand-mark"></span>
      <span class="brand-name">Tralvo GmbH</span>
    </div>
    <div class="divider"></div>

    <h1 class="headline">
      <span class="line-dark">Transporter und</span>
      <span class="line-steel">Bus Vermietung</span>
    </h1>
    <p class="tagline">Ohne Kaution Superpreise</p>
  </section>
</body>
</html>
```